Advertisement Design Project

Attached is the information I need in a big color ad

10X11 that will go in a weekly local paper.
I am open to color and graphics-no pictures of people please.

My logo is also attached, which I would like in the ad.

Sorry for the short notice-I just got a deal on the space and it is due Friday.

```html
<!DOCTYPE html>
<html lang="en">
<head>
<meta charset="utf-8">
<title>New Tax Laws – Estate Planning Workshop</title>
<link rel="stylesheet" href="https://fonts.googleapis.com/css2?family=Arimo:ital,wght@0,400;0,700;1,700&family=Roboto+Condensed:ital,wght@0,700;1,700&display=swap">
<style>
  :root {
    --stage: #0b0b0b;
    --board: #1d3a35;
    --board-light: #2c4d47;
    --board-dark: #15302b;
    --gold: #f3ad00;
    --cream: #fff4a8;
    --white: #ffffff;
    --rule: #b9c2bf;
  }
  * { margin: 0; padding: 0; box-sizing: border-box; }
  html, body { width: 1200px; height: 1000px; overflow: hidden; background: var(--stage); }
  .canvas { position: relative; width: 1200px; height: 1000px; background: var(--stage); }
  .ad {
    position: absolute; left: 170px; top: 26px; width: 860px; height: 945px;
    background: var(--board); color: var(--white);
    font-family: "Arimo", Arial, sans-serif;
  }
  .headline {
    position: absolute; left: 56px; top: 22px;
    font-family: "Arimo", Arial, sans-serif; font-weight: 700;
    font-size: 116px; line-height: 118px; color: var(--gold);
    letter-spacing: -1px;
  }
  .chalk-art {
    position: absolute; left: 410px; top: 70px; width: 450px; height: 370px;
    background: radial-gradient(ellipse at 55% 45%, var(--board-light) 0%, var(--board) 60%, var(--board-dark) 100%);
  }
  .questions {
    position: absolute; left: 36px; top: 400px; width: 470px;
    list-style: none; font-size: 16px; line-height: 22.3px;
  }
  .questions li { position: relative; padding-left: 14px; }
  .questions li::before { content: "•"; position: absolute; left: 0; }
  .invite {
    position: absolute; left: 535px; top: 566px;
    font-weight: 700; font-size: 34px; line-height: 33px;
  }
  .brand {
    position: absolute; left: 40px; top: 840px;
    display: flex; align-items: center; gap: 10px;
    font-family: "Roboto Condensed", Arial Narrow, sans-serif; font-weight: 700;
    font-size: 22px; color: var(--gold);
  }
  .brand-dot { width: 16px; height: 16px; border-radius: 50%; background: var(--gold); }
  .presenter { position: absolute; left: 286px; top: 730px; font-family: "Roboto Condensed", Arial Narrow, sans-serif; font-weight: 700; }
  .presenter .label { font-size: 16px; color: var(--white); }
  .presenter .name { font-size: 20px; color: var(--cream); margin-top: 4px; }
  .presenter .title { font-size: 12px; margin-left: 6px; }
  .presenter .address { font-size: 12px; color: var(--cream); margin-left: 16px; }
  .workshop {
    position: absolute; left: 277px; top: 817px; width: 236px; height: 102px;
    border: 1px solid var(--rule); padding: 18px 10px 0 9px;
    font-family: "Roboto Condensed", Arial Narrow, sans-serif; font-weight: 700;
    font-size: 11px; line-height: 14.5px; color: var(--cream);
  }
  .workshop .legend {
    position: absolute; left: 6px; top: -8px; padding: 0 3px; background: var(--board);
  }
  .workshop .venue { margin-top: 12px; }
  .closing { position: absolute; left: 579px; top: 752px; font-family: "Roboto Condensed", Arial Narrow, sans-serif; font-weight: 700; }
  .closing .lead { font-size: 20px; }
  .closing .sub { font-size: 12px; color: var(--gold); }
  .closing .rsvp { font-size: 20px; line-height: 24px; margin-top: 24px; }
  .closing .tagline { font-style: italic; font-size: 17px; margin-top: 18px; }
</style>
</head>
<body>
<div class="canvas">
  <section class="ad">
    <h1 class="headline">NEW<br>TAX<br>LAWS</h1>

    <div class="chalk-art" role="img" aria-label="Hand writing 'Trusts, Annuities and Long Term Care' in white chalk on a green chalkboard"></div>

    <ul class="questions">
      <li>Is my living Trust right for me?</li>
      <li>Does my existing Trust need to be changed?</li>
      <li>Why does Joint Tenancy create tax problems?</li>
      <li>I have a Will, isn’t that enough?</li>
      <li>Why do I need powers of attorney?</li>
      <li>How much are inheritance taxes?</li>
      <li>What are the new Affordable Care Act Taxes?</li>
      <li>How does Long Term Care insurance work?</li>
      <li>The average cost of long term care is over 80K a year-<br>how do I plan for those costs?</li>
      <li>The truth about annuities-</li>
      <li>What are the biggest mistakes in estate planning?</li>
    </ul>

    <p class="invite">Come learn<br>what you need<br>to know</p>

    <div class="brand"><span class="brand-dot"></span>Marsh Estate Law</div>

    <div class="presenter">
      <p class="label">Presented by:</p>
      <p class="name">dana ellis marsh<span class="title">Attorney at Law</span></p>
      <p class="address">412 Harbor Lane, Soquel.</p>
    </div>

    <div class="workshop">
      <span class="legend">Workshop Time / Place</span>
      <p>September 19, 2013, 1-2:30pm,&nbsp;&nbsp; 6-7:30pm</p>
      <p class="venue">Seaview Bay Inn, Aptos<br>2100 Cliffside Court<br>Aptos, California 95003</p>
    </div>

    <div class="closing">
      <p class="lead">Helping&nbsp; Families</p>
      <p class="sub">plan their estates for over 20 years.</p>
      <p class="rsvp">RSVP seating is limited:<br>(555) 014 - 2700</p>
      <p class="tagline">Be Smart. Plan Ahead.</p>
    </div>
  </section>
</div>
</body>
</html>
```